Präsentationsvorlagen für Start-up im Bereich Unternehmensberatung
Zielgruppe
Start-up im Bereich Unternehmensberatung. Zielgruppen sind CEO und HR Verantwortliche in Großunternehmen. Suchen klares, hochwertiges Design eher an Frauen als an Männer gerichtet. Haben bereits Vorlagen erarbeitet, diese sind aber zu technisch orientiert. Erwartet wird eine neue pptx Präsentation
Aufgabenstellung
Bilder / Texte gemäss Website respektive bestehender PPT.

```html
<!DOCTYPE html>
<html lang="de">
<head>
<meta charset="utf-8">
<title>Schlüsselfaktoren | Der Prozess</title>
<link rel="stylesheet" href="https://fonts.googleapis.com/css2?family=Roboto+Condensed:wght@400;700&family=Roboto:wght@400;700&display=swap">
<style>
  :root {
    --brand-red: #c00000;
    --ring-red: #c4000a;
    --ring-dark: #8e0008;
    --disc-grey: #eeeeee;
    --number-grey: #c2c2c2;
    --text-dark: #2b2b2b;
    --paper: #ffffff;
    --photo-light: #ece9e6;
    --photo-warm: #d9c8b8;
  }
  * { margin: 0; padding: 0; box-sizing: border-box; }
  html, body { width: 1200px; height: 711px; overflow: hidden; background: var(--paper); }
  .slide { position: relative; width: 1200px; height: 711px; background: var(--paper); font-family: "Roboto", Arial, sans-serif; }
  .key-photo {
    position: absolute; left: 0; top: 0; width: 392px; height: 711px;
    background: linear-gradient(160deg, var(--photo-warm) 0%, var(--photo-light) 35%, #f3f1ef 70%, #e6ddd3 100%);
  }
  .slide-title {
    position: absolute; left: 464px; top: 34px; width: 700px;
    font-family: "Roboto Condensed", Arial, sans-serif; font-weight: 400;
    font-size: 42px; letter-spacing: 0.5px; color: var(--brand-red); white-space: nowrap;
  }
  .process-diagram { position: absolute; left: 0; top: 0; width: 1200px; height: 711px; }
  .step-text { font-family: "Roboto", Arial, sans-serif; font-size: 13.5px; fill: var(--text-dark); text-anchor: middle; }
  .step-number { font-family: "Roboto", Arial, sans-serif; font-weight: 700; font-size: 46px; fill: var(--number-grey); text-anchor: middle; dominant-baseline: central; }
  .footer-name {
    position: absolute; left: 33px; top: 662px;
    font-family: "Roboto Condensed", Arial, sans-serif; font-weight: 700;
    font-size: 26px; color: var(--brand-red); letter-spacing: 0.5px;
  }
  .footer-rule { position: absolute; left: 130px; top: 678px; width: 1014px; height: 1px; background: var(--brand-red); }
  .page-number {
    position: absolute; left: 1160px; top: 669px;
    font-family: "Roboto", Arial, sans-serif; font-weight: 700; font-size: 14px; color: var(--brand-red);
  }
</style>
</head>
<body>
<div class="slide">
  <div class="key-photo" role="img" aria-label="Foto: Hand hält einen silbernen Schlüssel an einem Schlüsselring vor hellem Hintergrund"></div>

  <h1 class="slide-title">SCHLÜSSELFAKTOREN | DER PROZESS</h1>

  <svg class="process-diagram" viewBox="0 0 1200 711" aria-hidden="false">
    <defs>
      <filter id="soft-shadow" x="-30%" y="-30%" width="160%" height="160%">
        <feDropShadow dx="0" dy="3" stdDeviation="5" flood-color="#000" flood-opacity="0.35"/>
      </filter>
      <radialGradient id="ring-shade" cx="50%" cy="50%" r="50%">
        <stop offset="78%" stop-color="var(--ring-dark)"/>
        <stop offset="100%" stop-color="var(--ring-red)"/>
      </radialGradient>
    </defs>

    <!-- wave arcs -->
    <g fill="none" stroke="var(--ring-red)" stroke-width="10">
      <path d="M248 392 A138 138 0 0 0 524 392"/>
      <path d="M515 392 A138 138 0 0 1 791 392"/>
      <path d="M782 392 A138 138 0 0 0 1058 392"/>
    </g>

    <!-- step 1 -->
    <g class="step">
      <circle cx="386" cy="392" r="126" fill="var(--disc-grey)"/>
      <rect x="378" y="245" width="16" height="50" fill="var(--ring-red)"/>
      <circle cx="386" cy="197" r="57" fill="var(--ring-red)"/>
      <circle cx="386" cy="197" r="45" fill="var(--paper)" filter="url(#soft-shadow)"/>
      <text class="step-number" x="386" y="199">1</text>
      <circle cx="386" cy="392" r="105" fill="url(#ring-shade)"/>
      <circle cx="386" cy="392" r="84" fill="var(--paper)" filter="url(#soft-shadow)"/>
      <text class="step-text" x="386" y="362">
        <tspan x="386" dy="0">Kick-Off Vortrag</tspan>
        <tspan x="386" dy="17">u.a.  am Beispiel</tspan>
        <tspan x="386" dy="17">von Arbeitspausen</tspan>
        <tspan x="386" dy="17">“das habe ich mir</tspan>
        <tspan x="386" dy="17">jetzt aber verdient“</tspan>
      </text>
    </g>

    <!-- step 2 -->
    <g class="step">
      <circle cx="653" cy="392" r="126" fill="var(--disc-grey)"/>
      <rect x="645" y="490" width="16" height="52" fill="var(--ring-red)"/>
      <circle cx="653" cy="594" r="57" fill="var(--ring-red)"/>
      <circle cx="653" cy="594" r="45" fill="var(--paper)" filter="url(#soft-shadow)"/>
      <text class="step-number" x="653" y="596">2</text>
      <circle cx="653" cy="392" r="105" fill="url(#ring-shade)"/>
      <circle cx="653" cy="392" r="84" fill="var(--paper)" filter="url(#soft-shadow)"/>
      <text class="step-text" x="653" y="345">
        <tspan x="653" dy="0">Der Unterschied</tspan>
        <tspan x="653" dy="17">zwischen Willenskraft</tspan>
        <tspan x="653" dy="17">und Vorstellungs-</tspan>
        <tspan x="653" dy="17">vermögen, oder die</tspan>
        <tspan x="653" dy="17">Antworten auf die</tspan>
        <tspan x="653" dy="17">Frage nach dem</tspan>
        <tspan x="653" dy="17">Warum?</tspan>
      </text>
    </g>

    <!-- step 3 -->
    <g class="step">
      <circle cx="920" cy="392" r="126" fill="var(--disc-grey)"/>
      <rect x="912" y="247" width="16" height="50" fill="var(--ring-red)"/>
      <circle cx="920" cy="199" r="57" fill="var(--ring-red)"/>
      <circle cx="920" cy="199" r="45" fill="var(--paper)" filter="url(#soft-shadow)"/>
      <text class="step-number" x="920" y="201">3</text>
      <circle cx="920" cy="392" r="105" fill="url(#ring-shade)"/>
      <circle cx="920" cy="392" r="84" fill="var(--paper)" filter="url(#soft-shadow)"/>
      <text class="step-text" x="920" y="380">
        <tspan x="920" dy="0">Start des 6-</tspan>
        <tspan x="920" dy="17">monatigen</tspan>
        <tspan x="920" dy="17">Prozesses</tspan>
      </text>
    </g>
  </svg>

  <div class="footer-name">LUMIVA</div>
  <div class="footer-rule"></div>
  <div class="page-number">13</div>
</div>
</body>
</html>
```